Business Card Design Competition

We need a business card design for our Internet Marketing company. We require both front and back designs and the final card must be 89x53mm in size, plus crop marks to 91x55mm. Colours as per logo, plus perhaps black and/or grey (#828282).
Final text must be editable (if you can supply an editable Fireworks PNG, even better)...
FRONT TEXT:
Full Name
Position
Address Line
Suburb, State, Postcode
Phone: 0000 000 000
Mobile: 0000 000 000
Email: xxx@brimleafpromo.com.au
Web: www.brimleafpromo.com.au
Rear of card should be a fresh design plus our slogan text: "Getting You Noticed" in large font, then in small text "Brimleaf Holdings Pty Ltd (ABN: 42 563 701 384)".
Target Market(s)
Small/Medium Businesses
Industry/Entity Type
Business
Look and feel
Each slider illustrates characteristics of the customer's brand and the style your logo design should communicate.

```html
<!DOCTYPE html>
<html lang="en">
<head>
<meta charset="utf-8">
<title>Brimleaf Promo – Business Card</title>
<link href="https://fonts.googleapis.com/css2?family=Pathway+Gothic+One&display=swap" rel="stylesheet">
<style>
  :root {
    --page: #ffffff;
    --card: #3b3b3b;
    --band: #000000;
    --rule: #8a8a8a;
    --text: #d8d8d8;
    --accent: #d6e000;
    --ring: #f2b600;
  }
  * { margin: 0; padding: 0; box-sizing: border-box; }
  html, body { width: 1200px; height: 900px; overflow: hidden; background: var(--page); }
  body { position: relative; font-family: "Pathway Gothic One", "Arial Narrow", sans-serif; color: var(--text); }

  .card { position: absolute; left: 348px; width: 504px; height: 302px; background: var(--card); border: 1px solid #222; }
  .card--back { top: 102px; height: 300px; }
  .card--front { top: 482px; }

  .band { position: absolute; background: var(--band); display: flex; align-items: center; }
  .card--back .band { left: 0; top: 106px; width: 342px; height: 86px; justify-content: flex-end; padding-right: 14px; }
  .corner-mark { position: absolute; left: 376px; top: 106px; }

  .brand { display: flex; align-items: center; gap: 8px; }
  .brand__dot { width: 46px; height: 46px; border-radius: 50%; background: var(--ring); flex: none; }
  .brand__name { color: var(--accent); font-size: 24px; line-height: 1; letter-spacing: 0.5px; }

  .card--front .side-rule { position: absolute; left: 20px; top: 4px; width: 1px; height: 294px; background: var(--rule); }
  .card--front .mid-rule { position: absolute; left: 20px; top: 154px; width: 136px; height: 1px; background: var(--rule); }

  .address { position: absolute; left: 24px; top: 8px; font-size: 15px; }
  .phones { position: absolute; left: 24px; top: 40px; font-size: 11px; line-height: 12px; }
  .contact-web { position: absolute; left: 24px; top: 278px; font-size: 11px; }

  .name-box { position: absolute; left: 162px; top: 110px; width: 170px; height: 84px; background: var(--band); text-align: right; padding: 6px 10px 0 0; }
  .name-box__name { color: var(--accent); font-size: 38px; line-height: 40px; }
  .name-box__role { color: var(--accent); font-size: 24px; line-height: 26px; }

  .card--front .band { left: 338px; top: 110px; width: 166px; height: 84px; padding-left: 8px; }
  .card--front .brand__dot { width: 40px; height: 40px; }
  .card--front .brand__name { font-size: 22px; }
</style>
</head>
<body>
  <section class="card card--back" aria-label="Card back">
    <div class="band">
      <div class="brand">
        <span class="brand__dot"></span>
        <span class="brand__name">Brimleaf Promo</span>
      </div>
    </div>
    <svg class="corner-mark" width="24" height="24" viewBox="0 0 24 24" aria-hidden="true">
      <polygon points="0,0 24,0 24,24" fill="#000"/>
    </svg>
  </section>

  <section class="card card--front" aria-label="Card front">
    <span class="side-rule"></span>
    <span class="mid-rule"></span>
    <p class="address">14 Carrow Lane · Fenbury FN3 7QD</p>
    <p class="phones">Ph: +44 (0)20 7946 0132<br>Mobile: +44 (0)7700 900 418</p>
    <div class="name-box">
      <p class="name-box__name">Dana Whitlock</p>
      <p class="name-box__role">C.E.O.</p>
    </div>
    <div class="band">
      <div class="brand">
        <span class="brand__dot"></span>
        <span class="brand__name">Brimleaf Promo</span>
      </div>
    </div>
    <p class="contact-web">Email: xxx@brimleafpromo.com.au · Web: www.brimleafpromo.com.au</p>
  </section>
</body>
</html>
```